Petal Crate Guild - A Monthly Subscription for Essential Oils - Storevane Website Design

A monthly subscription company. Need a Storevane Website Design and uploaded to fully work with Brisk Renewals.

Please look at these sites for examples as well as the images I enclosed.

https://purelymeadow.com/
https://www.florant-xa.com/
https://www.dinnertrove.com/
https://www.globalsnackora.com/

```html
<!DOCTYPE html>
<html lang="en">
<head>
<meta charset="utf-8">
<title>Petal Crate Guild – Monthly Subscription for Essential Oils</title>
<link href="https://fonts.googleapis.com/css2?family=Roboto:wght@300;400;500;700&display=swap" rel="stylesheet">
<style>
:root{
  --orange:#f26b47;
  --taupe:#c3b9ac;
  --ink:#2b2b2b;
  --muted:#8a8a8a;
  --line:#e3e3e3;
  --panel:#f2f2f2;
  --footer:#111111;
  --white:#ffffff;
}
*{box-sizing:border-box;margin:0;padding:0}
html,body{width:684px;height:1200px;overflow:hidden;background:var(--white);font-family:'Roboto',Arial,sans-serif;color:var(--ink)}
.page{position:relative;width:684px;height:1200px}
.topbar{height:14px;background:var(--orange);color:var(--white);font-size:6px;text-align:center;line-height:14px;letter-spacing:.3px}
.header{position:relative;height:104px}
.search{position:absolute;left:50px;top:40px;width:126px;height:18px;border:1px solid #9a9a9a;display:flex;align-items:center;padding-left:6px;font-size:7px;color:var(--muted);gap:5px}
.brand{position:absolute;left:0;right:0;top:34px;text-align:center;font-size:22px;font-weight:400;color:var(--ink)}
.account{position:absolute;right:80px;top:45px;font-size:7px;color:var(--muted)}
.account span{margin:0 4px}
.bag{position:absolute;right:50px;top:38px}
.nav{position:absolute;left:0;right:0;top:96px;display:flex;justify-content:center;gap:26px;font-size:8px;color:#555}
.hero{position:relative;height:336px;margin-top:16px;background:linear-gradient(120deg,#3c3a30 0%,#6a6452 30%,#8a8572 50%,#5e5a44 72%,#2f2d24 100%);display:flex;flex-direction:column;align-items:center;justify-content:flex-start;color:var(--white);text-align:center}
.hero h1{margin-top:174px;font-size:26px;font-weight:400}
.hero p{margin-top:6px;font-size:11px;font-weight:300}
.btn{display:inline-block;background:var(--orange);color:var(--white);font-size:9px;padding:8px 18px;margin-top:16px}
.dots{display:flex;justify-content:center;gap:6px;margin-top:10px}
.dots i{width:4px;height:4px;border-radius:50%;background:#bbb}
.dots i.on{background:var(--orange)}
.plans{position:absolute;top:490px;left:0;width:684px;height:170px;background:var(--panel)}
.plan{position:absolute;top:16px;width:187px;height:121px;background:var(--taupe);color:var(--white);text-align:center;padding-top:23px}
.plan.featured{background:var(--orange)}
.plan h3{font-size:10px;font-weight:400;letter-spacing:1px;padding-bottom:8px;border-bottom:1px solid rgba(255,255,255,.5);margin:0 16px}
.plan strong{display:block;font-size:13px;font-weight:500;letter-spacing:1px;margin-top:12px}
.plan small{display:block;font-size:8px;letter-spacing:1px;margin-top:14px;padding-top:6px;border-top:1px solid rgba(255,255,255,.5);margin-left:60px;margin-right:60px}
.products{position:absolute;top:676px;left:50px;width:584px;display:flex;gap:8px}
.product{flex:1;border:1px solid var(--line);height:180px;padding:0 0 0 0}
.shot{height:98px;margin:6px}
.product .name{font-size:7px;color:var(--muted);margin:4px 8px 0}
.product .price{font-size:8px;color:var(--orange);margin:2px 8px 0}
.product .add{display:inline-block;background:var(--orange);color:var(--white);font-size:7px;padding:5px 8px;margin:8px 8px 0}
.footer{position:absolute;top:900px;left:0;width:684px;height:300px;background:var(--footer);color:#cfcfcf}
.col{position:absolute;top:40px;font-size:7px;line-height:1.45}
.col h4{color:var(--white);font-size:9px;font-weight:500;letter-spacing:.5px;margin-bottom:14px}
.blogimg{width:160px;height:90px;background:linear-gradient(160deg,#e9f2d8,#9cc476 55%,#4f7a3a)}
.blogtitle{color:var(--white);font-size:9px;font-weight:500;margin-top:6px}
.field{display:flex;margin-top:12px}
.field span{width:140px;height:20px;background:var(--white);color:var(--muted);font-size:6px;padding:6px}
.field b{width:20px;height:20px;background:var(--orange);display:flex;align-items:center;justify-content:center}
.social li{list-style:none;display:flex;align-items:center;gap:6px;margin-bottom:3px}
.social i{width:6px;height:6px;border-radius:50%;background:#cfcfcf;display:inline-block}
.copy{position:absolute;bottom:12px;left:0;right:0;text-align:center;font-size:6px;color:#aaa}
.page-no{position:absolute;right:10px;bottom:12px;font-size:6px;color:#aaa}
</style>
</head>
<body>
<div class="page">
  <div class="topbar">Free shipping on all annual subscription orders today</div>
  <header class="header">
    <div class="search"><svg width="8" height="8" viewBox="0 0 10 10"><circle cx="4" cy="4" r="3" fill="none" stroke="#333" stroke-width="1.3"/><line x1="6.3" y1="6.3" x2="9.3" y2="9.3" stroke="#333" stroke-width="1.3"/></svg>Search</div>
    <div class="brand">Petal Crate Guild</div>
    <div class="account">Sign in<span>|</span>Create Account<span>|</span>Checkout</div>
    <svg class="bag" width="18" height="22" viewBox="0 0 18 22"><path d="M2 6h14l-1 15H3z" fill="none" stroke="#333" stroke-width="1.3"/><path d="M6 8V4a3 3 0 0 1 6 0v4" fill="none" stroke="#333" stroke-width="1.3"/></svg>
    <nav class="nav"><span>Home</span><span>Shop</span><span>Subscription</span><span>About Us ▾</span><span>Contact Us</span></nav>
  </header>
  <section class="hero" role="img" aria-label="Essential oil bottles and dried flowers on a wooden table">
    <h1>Petal Crate Guild</h1>
    <p>Monthly Subscription for Essential Oils</p>
    <span class="btn">Shop Now</span>
  </section>
  <div class="dots" style="position:absolute;top:464px;left:0;right:0"><i class="on"></i><i></i><i></i></div>
  <section class="plans">
    <div class="plan" style="left:50px"><h3>ANNUAL SUBSCRIPTION</h3><strong>GET 50 % OFF</strong><small>VIEW ALL</small></div>
    <div class="plan featured" style="left:249px"><h3>MONTHLY SUBSCRIPTION</h3><strong>GET 10 % OFF</strong><small>VIEW ALL</small></div>
    <div class="plan" style="left:447px"><h3>6 MONTH SUBSCRIPTION</h3><strong>GET 20 % OFF</strong><small>VIEW ALL</small></div>
  </section>
  <section class="products">
    <div class="product"><div class="shot" role="img" aria-label="Amber dropper bottle beside white box" style="background:linear-gradient(90deg,#f3f3f3,#e4e4e4 50%,#8a4b2a 70%,#f3f3f3 85%)"></div><p class="name">PRODUCT NAME</p><p class="price">$50.00</p><span class="add">Add To Cart</span></div>
    <div class="product"><div class="shot" role="img" aria-label="Clear dropper bottle beside white box" style="background:linear-gradient(90deg,#f5f5f5,#e8e8e8 55%,#f0f0f0)"></div><p class="name">PRODUCT NAME</p><p class="price">$50.00</p><span class="add">Add To Cart</span></div>
    <div class="product"><div class="shot" role="img" aria-label="Oil bottle in open white gift box" style="background:linear-gradient(90deg,#dcdcdc,#efefef 40%,#6b4a2e 55%,#e6e6e6 70%)"></div><p class="name">PRODUCT NAME</p><p class="price">$50.00</p><span class="add">Add To Cart</span></div>
    <div class="product"><div class="shot" role="img" aria-label="Oil bottle in kraft and black box" style="background:linear-gradient(90deg,#e8d9bf,#2a2a2a 45%,#b07a3a 55%,#d9c6a2 75%)"></div><p class="name">PRODUCT NAME</p><p class="price">$50.00</p><span class="add">Add To Cart</span></div>
  </section>
  <footer class="footer">
    <div class="col" style="left:50px;width:120px"><h4>WELCOME</h4><p>Lorem ipsum dolor sit amet, consectetur adipiscing elit, sed do eiusmod tempor incididunt ut labore et dolore magna aliqua. Ut enim ad minim veniam, quis nostrud exercitation.</p></div>
    <div class="col" style="left:212px;width:160px"><h4>BLOG</h4><div class="blogimg" role="img" aria-label="Oil drop falling from a green leaf"></div><p class="blogtitle">Lorem ipsum dolor</p><p>Aug 20,2020 | By Admin</p><p>Lorem ipsum dolor sit amet, consectetur adipiscing elit, sed do eiusmod tempor.</p></div>
    <div class="col" style="left:372px;width:170px"><h4>NEWSLETTER</h4><p>Lorem ipsum dolor sit amet, consectetur adipiscing elit, sed do eiusmod tempor incididunt.</p><div class="field"><span>Email</span><b><svg width="8" height="8" viewBox="0 0 8 8"><path d="M1 4h6M4 1l3 3-3 3" fill="none" stroke="#fff" stroke-width="1.2"/></svg></b></div></div>
    <div class="col" style="left:580px;width:80px"><h4>FOLLOW US</h4><ul class="social"><li><i></i>Facelane</li><li><i></i>Chirpline</li><li><i></i>Viewtube</li><li><i></i>Snapgrid</li></ul></div>
    <p class="copy">Copyright© Company Name. 2020 | All Rights Reserved.</p>
    <span class="page-no">238</span>
  </footer>
</div>
</body>
</html>
```